Marlow Institute Counsellor iPhone app design

Live wireframes are here;

https://view.plankora.example/7c2e91a04d6b3f8e5a1c9d0b2e4f6a8c3d5e7f90#/pages/48210935

Password - marlowinst482!

We're nearing completion of the Blueprinting phase for our app development project for Marlow Institute. We need a designs matching the attached functional specification we've created for the app.

VISION
The Marlow Institute Counselling Services app provides simple and accessible information and engagement with mobile relevant services.
Opening the app, users are greeted with a simple “Hello, how are you today?” a 3 multiple choice answers to both aid in contextual content presentation/navigation specific to the users needs.
Users can access a range of existing web resources from the current website via live in app content and web links. Users can also access a personal folder storing PDF’s that are shared as part of meetings with Marlow Counsellors.
The app also features evolving content pulling from the existing WIKI and presents new and user relevant updates upon opening the app.
Finally, the solution will also deliver support to senior counsellors on each campus by streamlining tasks (such as booking appointments etc). The solution will also provide counsellors with notifications on students at risk and who may need greater support on their journeys.

Target Market(s)

People aged 15 to 24 years
• Students in this age group represent the largest market for
the industry, accounting for an estimated 44.7% of industry revenue in 2014-15. Demand for vocational education from school leavers has declined, as government reforms in higher education have led to more available university places for undergraduate students. Consequently, this market has declined in its share of revenue over the past five years.

People aged 25 to 44 years
• People aged 25 to 44 years are estimated to account for
37.2% of industry revenue. This market has grown its share of revenue over the past five years, as many Australians are entering the system to retrain or update workforce skills due to structural changes occurring in the economy. Students in this age group typically work full- time and therefore undertake their studies part-time, either on-campus or through distance learning.

People aged 45 years and over
• Individuals in this market represent 18.1% of the industry.
The majority of students in this age group have well- established careers, so students undertaking vocational courses are either seeking to upskill or have decided to change careers. As many of these students are employed full-time and often have family commitments, they require more flexible class schedules. This market has remained relatively stable as a share of revenue over the past five years.

Industry/Entity Type

Counsellor

Font styles to use
Sans Serif

Requirements
Must have
• The app needs to meet accessibility guidelines, so no text in images, nice flat design etc.
• The wireframes attached are not to spec, they're just a guide.
• Designs must meet the Apple interface guidelines and device specs for iPhone 4s, 5, 5s, 6 6+
• We also need an app store logo.
Nice to have
• NA

```html
<!DOCTYPE html>
<html lang="en">
<head>
<meta charset="utf-8">
<title>Marlow Institute Counsellor – App Screens</title>
<link rel="stylesheet" href="https://fonts.googleapis.com/css2?family=Open+Sans:wght@400;600&display=swap">
<style>
  :root {
    --page-bg: #ffffff;
    --ink: #333333;
    --ink-soft: #555555;
    --accent: #1ba1e2;
    --white: #ffffff;
    --divider: rgba(160, 160, 160, 0.35);
    --drawer: rgba(98, 98, 98, 0.86);
    --drawer-button: #a9a9a9;
    --bubble: rgba(232, 222, 212, 0.6);
    --screen-gradient: linear-gradient(165deg, #f4fbfb 0%, #e4f2f2 18%, #d3e3df 38%, #e6d8cc 62%, #f1d3bf 82%, #f2cdb5 100%);
  }
  * { box-sizing: border-box; margin: 0; padding: 0; }
  html, body { width: 1200px; height: 900px; overflow: hidden; background: var(--page-bg); }
  body { position: relative; font-family: "Open Sans", sans-serif; color: var(--ink); }

  .screen {
    position: absolute; top: 157px; height: 586px; overflow: hidden;
    background: var(--screen-gradient);
  }
  .screen--contacts { left: 163px; width: 320px; }
  .screen--menu { left: 697px; width: 330px; }

  .status-bar {
    position: absolute; top: 0; left: 0; right: 0; height: 18px;
    background: rgba(255, 255, 255, 0.9);
    font-size: 11.5px; font-weight: 600; color: #111;
  }
  .status-bar__signal { position: absolute; left: 5px; top: 2px; display: flex; align-items: center; gap: 4px; }
  .status-bar__dots { display: flex; gap: 1.5px; }
  .status-bar__dots i { width: 6px; height: 6px; border-radius: 50%; background: #111; display: block; }
  .status-bar__dots i.empty { background: none; border: 1px solid #111; }
  .status-bar__time { position: absolute; left: 0; right: 0; top: 1px; text-align: center; }
  .status-bar__battery { position: absolute; right: 6px; top: 1px; display: flex; align-items: center; gap: 4px; }
  .battery { width: 22px; height: 10px; border: 1px solid #111; position: relative; }
  .battery::before { content: ""; position: absolute; left: 1px; top: 1px; bottom: 1px; width: 9px; background: #111; }
  .battery::after { content: ""; position: absolute; right: -3px; top: 2px; width: 2px; height: 4px; background: #111; }

  .app-title { position: absolute; top: 38px; left: 0; right: 0; text-align: center; font-size: 17px; }
  .menu-toggle { position: absolute; top: 38px; width: 16px; }
  .screen--contacts .menu-toggle { left: 290px; }
  .screen--menu .menu-toggle { left: 300px; }

  .contact-list { position: absolute; top: 78px; left: 0; right: 0; list-style: none; }
  .contact { height: 119px; padding: 8px 20px 0; border-bottom: 1px solid var(--divider); position: relative; }
  .contact:last-child { border-bottom: none; }
  .contact__name { font-size: 21px; font-weight: 400; color: var(--accent); line-height: 28px; }
  .contact__text { font-size: 14px; line-height: 18px; color: var(--ink-soft); margin-top: 1px; }
  .contact__call { display: flex; align-items: center; gap: 9px; margin-top: 6px; font-size: 17.5px; color: var(--ink); }
  .service-dot { width: 24px; height: 24px; border-radius: 50%; background: var(--accent); }
  .contact__actions { position: absolute; right: 20px; bottom: 12px; display: flex; gap: 8px; }
  .contact__actions.first { bottom: 13px; }
  .action { width: 28px; height: 28px; border-radius: 50%; background: var(--white); display: flex; align-items: center; justify-content: center; }

  .home-greeting { position: absolute; top: 162px; left: 0; right: 0; text-align: center; font-size: 19px; line-height: 24px; color: var(--ink-soft); }
  .bubble {
    position: absolute; width: 106px; height: 106px; border-radius: 50%;
    background: var(--bubble); border: 1px solid rgba(255,255,255,0.5);
    display: flex; flex-direction: column; align-items: center; justify-content: center;
    font-size: 13.5px; line-height: 14px; color: var(--ink-soft); text-align: center;
  }
  .bubble--talk { left: 47px; top: 245px; }
  .bubble--articles { left: 177px; top: 245px; }
  .bubble--blog { left: 110px; top: 353px; }
  .bubble__icon { width: 26px; height: 26px; border-radius: 50%; background: rgba(150,150,150,0.5); margin-bottom: 8px; }

  .drawer { position: absolute; top: 0; left: 0; width: 282px; height: 100%; background: var(--drawer); }
  .drawer__status { position: absolute; top: 0; left: 0; right: 0; height: 18px; background: rgba(120,120,120,0.35); }
  .profile { position: absolute; top: 30px; left: 22px; display: flex; align-items: center; gap: 13px; color: var(--white); }
  .profile__avatar { width: 43px; height: 43px; border-radius: 50%; background: radial-gradient(circle at 50% 40%, #d9c7a8, #8a7a66); border: 2px solid rgba(255,255,255,0.6); }
  .profile__name { font-size: 17px; line-height: 21px; }
  .profile__email { font-size: 12.5px; line-height: 15px; }
  .settings { position: absolute; top: 33px; left: 244px; width: 18px; }
  .drawer-menu { position: absolute; top: 117px; left: 15px; list-style: none; }
  .drawer-menu li { width: 252px; height: 27px; margin-bottom: 13.5px; background: var(--drawer-button); color: var(--white); font-size: 14px; font-weight: 600; letter-spacing: 1px; line-height: 27px; padding-left: 18px; border: 1px solid rgba(255,255,255,0.25); }
</style>
</head>
<body>

<section class="screen screen--contacts" aria-label="Contacts screen">
  <div class="status-bar">
    <div class="status-bar__signal"><span class="status-bar__dots"><i></i><i></i><i></i><i></i><i class="empty"></i></span>SIGNAL
      <svg width="13" height="10" viewBox="0 0 13 10"><path d="M1 3.5a8 8 0 0 1 11 0M3 5.7a5 5 0 0 1 7 0M6.5 9l1.6-1.6a2.3 2.3 0 0 0-3.2 0z" fill="none" stroke="#111" stroke-width="1.5"/></svg></div>
    <div class="status-bar__time">8:16 AM</div>
    <div class="status-bar__battery">50% <span class="battery"></span></div>
  </div>
  <h1 class="app-title">Welcome</h1>
  <svg class="menu-toggle" viewBox="0 0 16 12" height="12"><path d="M0 1h16M0 6h16M0 11h16" stroke="#333" stroke-width="1.5"/></svg>

  <ul class="contact-list">
    <li class="contact">
      <h2 class="contact__name">Harlow Vale</h2>
      <p class="contact__text">Lorem ipsum dolor sit amet, consectetur adipiscing elit. .</p>
      <p class="contact__call"><span class="service-dot"></span>02 5550 1234</p>
      <div class="contact__actions first">
        <span class="action"><svg width="14" height="20" viewBox="0 0 14 20"><path d="M7 0a7 7 0 0 0-7 7c0 5 7 13 7 13s7-8 7-13a7 7 0 0 0-7-7z" fill="#1ba1e2"/><circle cx="7" cy="7" r="3" fill="#fff"/><circle cx="7" cy="7" r="1.5" fill="#1ba1e2"/></svg></span>
        <span class="action"><svg width="16" height="16" viewBox="0 0 24 24"><path d="M6.6 10.8a15 15 0 0 0 6.6 6.6l2.2-2.2a1 1 0 0 1 1-.25 11.4 11.4 0 0 0 3.6.6 1 1 0 0 1 1 1V20a1 1 0 0 1-1 1A17 17 0 0 1 3 4a1 1 0 0 1 1-1h3.5a1 1 0 0 1 1 1c0 1.25.2 2.45.6 3.6a1 1 0 0 1-.25 1z" fill="#1ba1e2"/></svg></span>
      </div>
    </li>
    <li class="contact">
      <h2 class="contact__name">Harlow Vale</h2>
      <p class="contact__text">Lorem ipsum dolor sit amet, consectetur adipiscing elit. .</p>
      <p class="contact__call"><span class="service-dot"></span>02 5550 1234</p>
      <div class="contact__actions">
        <span class="action"><svg width="14" height="20" viewBox="0 0 14 20"><path d="M7 0a7 7 0 0 0-7 7c0 5 7 13 7 13s7-8 7-13a7 7 0 0 0-7-7z" fill="#1ba1e2"/><circle cx="7" cy="7" r="3" fill="#fff"/><circle cx="7" cy="7" r="1.5" fill="#1ba1e2"/></svg></span>
        <span class="action"><svg width="16" height="16" viewBox="0 0 24 24"><path d="M6.6 10.8a15 15 0 0 0 6.6 6.6l2.2-2.2a1 1 0 0 1 1-.25 11.4 11.4 0 0 0 3.6.6 1 1 0 0 1 1 1V20a1 1 0 0 1-1 1A17 17 0 0 1 3 4a1 1 0 0 1 1-1h3.5a1 1 0 0 1 1 1c0 1.25.2 2.45.6 3.6a1 1 0 0 1-.25 1z" fill="#1ba1e2"/></svg></span>
      </div>
    </li>
    <li class="contact">
      <h2 class="contact__name">Harlow Vale</h2>
      <p class="contact__text">Lorem ipsum dolor sit amet, consectetur adipiscing elit. .</p>
      <p class="contact__call"><span class="service-dot"></span>02 5550 1234</p>
      <div class="contact__actions">
        <span class="action"><svg width="14" height="20" viewBox="0 0 14 20"><path d="M7 0a7 7 0 0 0-7 7c0 5 7 13 7 13s7-8 7-13a7 7 0 0 0-7-7z" fill="#1ba1e2"/><circle cx="7" cy="7" r="3" fill="#fff"/><circle cx="7" cy="7" r="1.5" fill="#1ba1e2"/></svg></span>
        <span class="action"><svg width="16" height="16" viewBox="0 0 24 24"><path d="M6.6 10.8a15 15 0 0 0 6.6 6.6l2.2-2.2a1 1 0 0 1 1-.25 11.4 11.4 0 0 0 3.6.6 1 1 0 0 1 1 1V20a1 1 0 0 1-1 1A17 17 0 0 1 3 4a1 1 0 0 1 1-1h3.5a1 1 0 0 1 1 1c0 1.25.2 2.45.6 3.6a1 1 0 0 1-.25 1z" fill="#1ba1e2"/></svg></span>
      </div>
    </li>
    <li class="contact">
      <h2 class="contact__name">Harlow Vale</h2>
      <p class="contact__text">Lorem ipsum dolor sit amet, consectetur adipiscing elit. .</p>
      <p class="contact__call"><span class="service-dot"></span>02 5550 1234</p>
      <div class="contact__actions">
        <span class="action"><svg width="14" height="20" viewBox="0 0 14 20"><path d="M7 0a7 7 0 0 0-7 7c0 5 7 13 7 13s7-8 7-13a7 7 0 0 0-7-7z" fill="#1ba1e2"/><circle cx="7" cy="7" r="3" fill="#fff"/><circle cx="7" cy="7" r="1.5" fill="#1ba1e2"/></svg></span>
        <span class="action"><svg width="16" height="16" viewBox="0 0 24 24"><path d="M6.6 10.8a15 15 0 0 0 6.6 6.6l2.2-2.2a1 1 0 0 1 1-.25 11.4 11.4 0 0 0 3.6.6 1 1 0 0 1 1 1V20a1 1 0 0 1-1 1A17 17 0 0 1 3 4a1 1 0 0 1 1-1h3.5a1 1 0 0 1 1 1c0 1.25.2 2.45.6 3.6a1 1 0 0 1-.25 1z" fill="#1ba1e2"/></svg></span>
      </div>
    </li>
  </ul>
</section>

<section class="screen screen--menu" aria-label="Home screen with open navigation drawer">
  <div class="status-bar">
    <div class="status-bar__signal"><span class="status-bar__dots"><i></i><i></i><i></i><i></i><i class="empty"></i></span>SIGNAL
      <svg width="13" height="10" viewBox="0 0 13 10"><path d="M1 3.5a8 8 0 0 1 11 0M3 5.7a5 5 0 0 1 7 0M6.5 9l1.6-1.6a2.3 2.3 0 0 0-3.2 0z" fill="none" stroke="#111" stroke-width="1.5"/></svg></div>
    <div class="status-bar__time">8:16 AM</div>
    <div class="status-bar__battery">50% <span class="battery"></span></div>
  </div>
  <h1 class="app-title">Welcome</h1>
  <svg class="menu-toggle" viewBox="0 0 16 12" height="12"><path d="M0 1h16M0 6h16M0 11h16" stroke="#333" stroke-width="1.5"/></svg>
  <p class="home-greeting">Good morning,<br>how can we help?</p>
  <div class="bubble bubble--talk"><span class="bubble__icon"></span>Talk to<br>Someone</div>
  <div class="bubble bubble--articles"><span class="bubble__icon"></span>Articles</div>
  <div class="bubble bubble--blog"><span class="bubble__icon"></span>Blog</div>

  <nav class="drawer" aria-label="Main menu">
    <div class="drawer__status"></div>
    <div class="profile">
      <div class="profile__avatar" role="img" aria-label="User profile photo"></div>
      <div>
        <p class="profile__name">Cal Renwick</p>
        <p class="profile__email">cal@marlow.example</p>
      </div>
    </div>
    <svg class="settings" viewBox="0 0 24 24" height="18"><path d="M12 8.5a3.5 3.5 0 1 0 0 7 3.5 3.5 0 0 0 0-7zm9 5v-3l-2.3-.5a7 7 0 0 0-.8-1.9l1.3-2-2.1-2.1-2 1.3a7 7 0 0 0-1.9-.8L12.7 2h-3l-.5 2.5a7 7 0 0 0-1.9.8l-2-1.3-2.1 2.1 1.3 2a7 7 0 0 0-.8 1.9L1.5 10.5v3l2.2.5a7 7 0 0 0 .8 1.9l-1.3 2 2.1 2.1 2-1.3a7 7 0 0 0 1.9.8l.5 2.5h3l.5-2.5a7 7 0 0 0 1.9-.8l2 1.3 2.1-2.1-1.3-2a7 7 0 0 0 .8-1.9z" fill="#fff" fill-rule="evenodd"/></svg>
    <ul class="drawer-menu">
      <li>HOME</li>
      <li>ARTICLES</li>
      <li>CONTACTS</li>
      <li>PROFILE</li>
      <li>ABOUT</li>
    </ul>
  </nav>
</section>

</body>
</html>
```